Kitchen and Bathroom Remodeling Flyer

This flyer is for a home remodeling company that remodels peoples kitchens and bathrooms.

We want a flyer to be sophisticated: nice professional design with classy font.

FRONT OF FLYER:

I have attached the front flyer I created and there is no design to it. The reason is so you can see what text elements we want on the flyer. a second attachment has the text for easy copy and paste.

I like the idea of mentioning “Owners live in Ahwatukee” because this flyer will be passed around door to door in that town of Ahwatukee.

Please use the image and the corresponding headline specific to that image. The headline can be in the image or to the top of the image.

BACK OF FLYER:
The back of flyer is essentially a written letter with a profile image of our owners and then two testimonials at bottom. I’d like to add a little bit of design to the back of the flyer. See attachment for pdf of current text and basic structure.

Our brand colors are gray and blue# 0000cc

Our website is https://Kelmbrookrenovating.com

Thank you,
Tobias

Target Market(s)

Mostly woman. Homeowners making 100k+ a year that want to remodel their kitchen or bathroom

Industry/Entity Type

Home Improvement

Font styles to use
Serif
Sans Serif
Decorative

Colors

Designer to choose colors to be used in the design.

Requirements
Must have
• This has to be in photoshop with each element editable (I’ll want to change things down the road)
Nice to have
• Examples that I don’t want copied but so you have a rough idea of some design structure that I like:
• https://flyer.pixelvantyard.com/contest.aspx?id=5190362
• https://flyer.pixelvantyard.com/contest.aspx?id=627053
• https://flyer.pixelvantyard.com/contest.aspx?id=8831475
• https://www.pixelvantyard.com/design/42957018
• https://www.pixelvantyard.com/design/7160243
Should not have
• Nothing silly or too loud. Thank you

```html
<!DOCTYPE html>
<html lang="en">
<head>
<meta charset="utf-8">
<title>Kelmbrook Renovating Flyer</title>
<link href="https://fonts.googleapis.com/css2?family=Montserrat:wght@500;700;800&family=Arimo:wght@400;700&family=Patrick+Hand&display=swap" rel="stylesheet">
<style>
  :root{
    --blue:#1aa3f0;
    --brand-blue:#0000cc;
    --charcoal:#3b3a3a;
    --ink:#2b2b2b;
    --gray:#6d6d6d;
    --paper:#ffffff;
    --bg:#e6e6e4;
  }
  *{box-sizing:border-box;margin:0;padding:0}
  html,body{width:1200px;height:870px;overflow:hidden;background:var(--bg)}
  body{position:relative;font-family:"Arimo",Arial,sans-serif;color:var(--ink)}
  .flyer{position:absolute;top:72px;width:560px;height:725px;background:var(--paper);overflow:hidden;box-shadow:0 6px 18px rgba(0,0,0,.18)}
  .flyer--front{left:30px}
  .flyer--back{left:610px}
  .abs{position:absolute}
  .accent-bar{left:0;top:0;width:100%;height:7px;background:var(--blue)}
  .hl{color:var(--blue)}

  /* FRONT */
  .locale-tab{left:190px;top:13px;height:24px;width:200px;background:var(--charcoal);color:#fff;font:500 11px "Montserrat",sans-serif;display:flex;align-items:center;justify-content:center;clip-path:polygon(8% 0,100% 0,92% 100%,0 100%)}
  .headline{left:22px;top:40px;font:800 37px/1 "Montserrat",sans-serif;color:var(--charcoal);letter-spacing:-.5px}
  .photo{border:3px solid #fff}
  .photo--bath{left:20px;top:96px;width:200px;height:196px;background:linear-gradient(160deg,#d9d4cc,#7a6656 55%,#3f3833)}
  .photo--kitchen{left:205px;top:152px;width:335px;height:246px;background:linear-gradient(150deg,#f4f3ef,#cfd1d1 50%,#9a9c9b);box-shadow:0 2px 8px rgba(0,0,0,.2)}
  .caption{font:700 17px/1.05 "Montserrat",sans-serif;color:var(--charcoal);text-transform:uppercase}
  .caption--spa{left:280px;top:96px;width:250px}
  .caption--kitchen{left:24px;top:304px;width:180px}
  .promise-band{left:0;top:412px;width:330px;height:44px;background:var(--charcoal);clip-path:polygon(0 0,100% 0,92% 100%,0 100%);color:#fff;font:800 25px/44px "Montserrat",sans-serif;padding-left:20px}
  .promise-list{list-style:none;font-size:11.5px;line-height:1.3;color:var(--ink)}
  .promise-list li{padding-left:10px;position:relative;margin-bottom:3px}
  .promise-list li::before{content:"\2022";position:absolute;left:0}
  .promise-list--left{left:22px;top:466px;width:260px}
  .promise-list--right{left:340px;top:416px;width:205px}
  .photo--living{left:20px;top:548px;width:260px;height:160px;background:linear-gradient(135deg,#e7d2a6,#8a5a36 55%,#4a3020)}
  .brand{left:300px;top:590px;width:245px;text-align:left}
  .brand-mark{display:flex;align-items:center;gap:8px;font:700 18px "Montserrat",sans-serif;color:var(--brand-blue)}
  .brand-mark .dot{width:14px;height:14px;background:var(--brand-blue);border-radius:50%}
  .contact{margin-top:10px;font:700 13px "Arimo",sans-serif;color:var(--ink);display:flex;align-items:center;gap:6px}
  .contact svg{width:14px;height:14px}
  .credentials{margin-top:6px;font-size:9px;color:var(--blue);letter-spacing:1px}

  /* BACK */
  .title-box{left:250px;top:0;width:310px;height:104px;background:var(--charcoal);clip-path:polygon(0 0,100% 0,100% 100%,18% 100%);color:#fff;font:800 22px/1.05 "Montserrat",sans-serif;text-align:right;padding:14px 18px 0 0}
  .title-rule{left:0;top:96px;width:260px;height:5px;background:var(--blue)}
  .letter{left:30px;top:118px;width:505px;font:11.6px/1.3 "Patrick Hand",cursive;color:var(--ink)}
  .letter p{margin-bottom:6px}
  .portrait{left:36px;top:452px;width:112px;height:112px;border-radius:50%;background:radial-gradient(circle at 50% 40%,#e9d2be,#2f6fd0 70%,#dfe9f7)}
  .signoff{left:175px;top:452px;width:180px;font:11.6px/1.3 "Patrick Hand",cursive}
  .signoff p{margin-bottom:6px}
  .reviews-box{left:370px;top:455px;width:190px;height:64px;background:var(--charcoal);clip-path:polygon(14% 0,100% 0,100% 100%,0 100%);color:#fff;font:800 15px/1.05 "Montserrat",sans-serif;text-align:right;padding:8px 14px 0 0}
  .review{width:235px;display:flex;gap:10px;align-items:flex-start;font-size:9.5px;line-height:1.3}
  .review--one{left:30px;top:600px}
  .review--two{left:290px;top:560px}
  .review .avatar{flex:0 0 64px;height:64px;border-radius:50%;background:linear-gradient(135deg,#c9b39b,#5b4a3e)}
  .review--two .avatar{background:linear-gradient(135deg,#dfe6ee,#8497ab)}
  .review .quote-mark{color:var(--blue);font:800 26px/1 "Montserrat",sans-serif;height:18px}
  .review .author{margin-top:4px;font-weight:700}
  .review .place{color:var(--gray);font-size:8.5px}
</style>
</head>
<body>

<section class="flyer flyer--front">
  <div class="abs accent-bar"></div>
  <div class="abs locale-tab">Owners live in Ahwatukee</div>
  <h1 class="abs headline">Create Your <span class="hl">Dream</span> Space</h1>
  <div class="abs photo photo--bath" role="img" aria-label="Remodeled bathroom with dark wood vanity and glass shower"></div>
  <div class="abs photo photo--kitchen" role="img" aria-label="Bright white kitchen with island and pastries on the counter"></div>
  <p class="abs caption caption--spa">Turn an old bathroom into your own <span class="hl">personal spa</span></p>
  <p class="abs caption caption--kitchen"><span class="hl">Entertain</span> in a kitchen you'll <span class="hl">love</span> showing off to friends and family</p>
  <h2 class="abs promise-band">Our Client <span class="hl">Promises:</span></h2>
  <ul class="abs promise-list promise-list--left">
    <li>Provide <span class="hl">honest</span> and <span class="hl">straight forward</span> advice</li>
    <li>Return calls and show up <span class="hl">on time</span></li>
    <li>Employ <span class="hl">professional, respectful</span> and <span class="hl">knowledgeable</span> employees</li>
  </ul>
  <ul class="abs promise-list promise-list--right">
    <li><span class="hl">Respect</span> your home and ensure we keep it <span class="hl">clean</span></li>
    <li>Provide <span class="hl">clear expectations</span> of project timelines and pricing</li>
    <li>Create your <span class="hl">dream</span> living space with <span class="hl">great</span> attention to detail</li>
  </ul>
  <div class="abs photo photo--living" role="img" aria-label="Open kitchen and dining room with wood cabinets and hardwood floor"></div>
  <div class="abs brand">
    <div class="brand-mark"><span class="dot"></span>Kelmbrook Renovating</div>
    <div class="contact">
      <svg viewBox="0 0 24 24" aria-hidden="true"><circle cx="12" cy="12" r="12" fill="#0000cc"/><path d="M8 6l2 3-1.2 1.5a8 8 0 0 0 4.7 4.7L15 14l3 2-1 2.5c-5 0-10-5-10-10z" fill="#fff"/></svg>
      480-555-0173 &nbsp; Kelmbrookrenovating.com
    </div>
    <div class="credentials">LICENSED • BONDED • INSURED • ROC 408215</div>
  </div>
</section>

<section class="flyer flyer--back">
  <h2 class="abs title-box">Everyone wants<br>a <span class="hl">dream home</span><br>they can be<br><span class="hl">proud</span> of</h2>
  <div class="abs title-rule"></div>
  <div class="abs letter">
    <p>Dear Ahwatukee Homeowners,</p>
    <p>Everyone wants a dream home they can be proud of. We all want to feel prosperous in life and our home is an extension of ourselves, our style and feeling successful.</p>
    <p>We understand working with a remodeling contractor can be frustrating because they show up late, change the price and make a mess of your home.</p>
    <p>Kelmbrook Renovating is the most organized remodeling company in the valley and we'll create the dream space you'll be proud to show off to your friends, family &amp; neighbors.</p>
    <p>One of our co-founders Tobias has been through several contractor nightmares and it is the main reason Tobias, Callum and Desmond founded Kelmbrook Renovating.</p>
    <p>We are an award-winning home remodeling licensed contractor that is known for showing up on time, being organized, clearly explaining all aspects of the remodel, adhering to project budget and timeline.</p>
    <p>One of our clients said we were the AutoVista of home remodeling and we think that's a nice comparison. We'll guide you through our 4 step process and there's no haggle, no sales BS and our clients love the experience.</p>
  </div>
  <div class="abs portrait" role="img" aria-label="Portrait of a company co-founder in a blue shirt"></div>
  <div class="abs signoff">
    <p>To a beautiful home you'll love showing off to your neighbors, family &amp; friends,</p>
    <p>Tobias, Callum and Desmond</p>
    <p>Kelmbrook Renovating<br>ROC 408215<br>Kelmbrookrenovating.com<br>480-555-0173</p>
  </div>
  <h3 class="abs reviews-box">See what our<br><span class="hl">customers</span><br>are saying</h3>
  <div class="abs review review--one">
    <div class="avatar" role="img" aria-label="Photo of a smiling couple"></div>
    <div>
      <div class="quote-mark">&ldquo;</div>
      <p>Callum and his team were easy to work with and paid attention to detail every step. Our kitchen looks perfect and the crew kept our home clean. Thank you Kelmbrook Renovating!</p>
      <p class="author">Marissa &amp; Owen T.</p>
      <p class="place">Chandler, AZ</p>
    </div>
  </div>
  <div class="abs review review--two">
    <div class="avatar" role="img" aria-label="Photo of a happy couple outdoors"></div>
    <div>
      <div class="quote-mark">&ldquo;</div>
      <p>Our bathroom is stunning! The crew was polite, kept us informed and finished on schedule. We are very happy and would hire them again. Thank you!</p>
      <p class="author">Lena and Hugo R.</p>
      <p class="place">Ahwatukee, AZ</p>
    </div>
  </div>
</section>

</body>
</html>
```